Become a real French Pastry chef with an easy 3 step pastry kit box.

The company is specialized in French pastries and the boxes will be sold online, and retail stores. The goal is for anyone who likes to be creative and crafty to create and bake their own traditional french pastry in 3 easy steps right at home. French pastries can be known to take hours to bake. These boxes allow you to make them very quickly, no hassle and they results taste amazing. All the ingredients are from FRANCE. Everything you need is in the box, All you need is water! The box design desired is elegant, simple, glamorous but yet eye catchy for retail distribution. This is a kit box with pre scaled ingredients to make your own eclairs. Box dimensions are 8x6x2.
Updates

Target Market(s)

Middle Aged, middle to upper class housewives who enjoy cooking and baking

Industry/Entity Type

Bakery

Font styles to use
Decorative
Script

Colors

Designer to choose colors to be used in the design.

Requirements
Must have
• This box will be called "The eclair kit by {logo}, or {logo} presents the Eclair kit.
• Has to have the instructions (attached document)
• "This box contains: 4 éclair shells, powder pouch, icing bag, pipping bag and pipping tip"
• Net weight 245g
• Nutrition label (attached)
Nice to have
• An eclair on it.

```html
<!DOCTYPE html>
<html lang="en">
<head>
<meta charset="utf-8">
<title>The Eclair Kit – Box Dieline</title>
<link rel="stylesheet" href="https://fonts.googleapis.com/css2?family=Oswald:wght@600;700&family=Roboto:wght@400;500;700&family=Great+Vibes&display=swap">
<style>
  :root {
    --paper: #f8f8f7;
    --cut-line: #8e8e8e;
    --ink: #1d1d1d;
    --cocoa: #3a2a28;
    --cocoa-soft: #8a6c64;
    --brand-blue: #3a63c9;
    --hand-blue: #2d6f8e;
    --hand-gold: #e7a728;
    --hand-red: #a8201f;
    --white-card: rgba(255,255,255,0.82);
  }
  html, body {
    margin: 0;
    padding: 0;
    width: 1200px;
    height: 1200px;
    overflow: hidden;
    background: #ffffff;
  }
  .dieline { display: block; width: 1200px; height: 1200px; }
  .panel { fill: var(--paper); stroke: var(--cut-line); stroke-width: 1.2; }
  .fold { fill: none; stroke: var(--cut-line); stroke-width: 1; }
  .dotted-frame { fill: none; stroke: #333; stroke-width: 1; stroke-dasharray: 2 3; }
  .kit-title { font-family: 'Oswald', sans-serif; font-weight: 700; fill: var(--ink); letter-spacing: 0.5px; }
  .kit-title--light { fill: #ffffff; }
  .brand-name { font-family: 'Roboto', sans-serif; font-weight: 500; fill: var(--brand-blue); }
  .brand-dot { fill: none; stroke: var(--brand-blue); stroke-width: 1.4; }
  .presents { font-family: 'Great Vibes', cursive; fill: #ffffff; }
  .item-label { font-family: 'Roboto', sans-serif; font-weight: 500; font-size: 8px; fill: #333; letter-spacing: 0.3px; }
  .step-text { font-family: 'Roboto', sans-serif; font-size: 10.2px; fill: #222; }
  .ingredients { font-family: 'Roboto', sans-serif; font-size: 6.3px; fill: #2a2a2a; }
  .nutrition { font-family: 'Roboto', sans-serif; font-size: 6px; fill: #111; }
  .nutrition-head { font-family: 'Roboto', sans-serif; font-weight: 700; font-size: 12px; fill: #111; }
  .nutrition-bold { font-weight: 700; }
  .step-card { fill: var(--white-card); }
  .label-plate { fill: var(--cocoa); }
  .label-border { fill: none; stroke: #ffffff; stroke-width: 2; stroke-dasharray: 1.5 3; }
  .wash { mix-blend-mode: multiply; }
</style>
</head>
<body>
<svg class="dieline" viewBox="0 0 1500 1500" xmlns="http://www.w3.org/2000/svg">
  <defs>
    <radialGradient id="wash-blue" cx="50%" cy="50%" r="50%">
      <stop offset="0" stop-color="#7fc7f0" stop-opacity="0.55"/>
      <stop offset="0.6" stop-color="#a9d9f4" stop-opacity="0.25"/>
      <stop offset="1" stop-color="#ffffff" stop-opacity="0"/>
    </radialGradient>
    <radialGradient id="wash-pink" cx="50%" cy="50%" r="50%">
      <stop offset="0" stop-color="#f59bc0" stop-opacity="0.5"/>
      <stop offset="0.6" stop-color="#f7bdd5" stop-opacity="0.22"/>
      <stop offset="1" stop-color="#ffffff" stop-opacity="0"/>
    </radialGradient>
    <radialGradient id="wash-yellow" cx="50%" cy="50%" r="50%">
      <stop offset="0" stop-color="#f4e64f" stop-opacity="0.6"/>
      <stop offset="0.6" stop-color="#f7ee8f" stop-opacity="0.25"/>
      <stop offset="1" stop-color="#ffffff" stop-opacity="0"/>
    </radialGradient>
    <radialGradient id="wash-red" cx="50%" cy="50%" r="50%">
      <stop offset="0" stop-color="#f46a55" stop-opacity="0.5"/>
      <stop offset="0.6" stop-color="#f7a294" stop-opacity="0.22"/>
      <stop offset="1" stop-color="#ffffff" stop-opacity="0"/>
    </radialGradient>
    <radialGradient id="scene-fade" cx="50%" cy="50%" r="70%">
      <stop offset="0" stop-color="#f5f5f5"/>
      <stop offset="1" stop-color="#bcbcbc"/>
    </radialGradient>
    <radialGradient id="pastry-tone" cx="40%" cy="45%" r="55%">
      <stop offset="0" stop-color="#b47440"/>
      <stop offset="0.55" stop-color="#7a4022"/>
      <stop offset="0.85" stop-color="#3d2220" stop-opacity="0.85"/>
      <stop offset="1" stop-color="#3d2220" stop-opacity="0"/>
    </radialGradient>
    <linearGradient id="items-tone" x1="0" y1="0" x2="1" y2="1">
      <stop offset="0" stop-color="#dbe5f6"/>
      <stop offset="1" stop-color="#f6dae8"/>
    </linearGradient>
    <linearGradient id="lettering-tone" x1="0" y1="0" x2="1" y2="0">
      <stop offset="0" stop-color="#c455c9"/>
      <stop offset="1" stop-color="#f08a6a"/>
    </linearGradient>
    <clipPath id="box-clip">
      <rect x="42" y="276" width="623" height="949"/>
      <rect x="665" y="250" width="175" height="1000"/>
      <rect x="845" y="80" width="420" height="1340"/>
      <rect x="1265" y="250" width="177" height="1000"/>
    </clipPath>
  </defs>

  <!-- ===== LID (left) ===== -->
  <g class="lid">
    <path class="panel" d="M235,280 C120,280 42,360 42,470 V1040 C42,1150 120,1225 235,1225 Z"/>
    <path class="fold" d="M222,295 C130,300 62,370 62,458 V1045 C62,1135 130,1205 222,1210"/>
    <path class="panel" d="M245,290 Q245,276 260,276 H650 Q664,276 664,292 V468 H245 Z"/>
    <path class="panel" d="M245,1030 H664 V1208 Q664,1224 650,1224 H260 Q245,1224 245,1208 Z"/>
    <rect class="panel" x="235" y="468" width="430" height="562"/>
    <rect x="235" y="468" width="430" height="562" fill="url(#scene-fade)" role="img" aria-label="Soft grey sketch of a French bakery kitchen with shelves and ovens"/>
  </g>

  <!-- ===== FRONT STRIP ===== -->
  <g class="front-strip">
    <rect class="panel" x="665" y="250" width="175" height="205"/>
    <rect class="panel" x="665" y="1050" width="175" height="200"/>
    <rect class="panel" x="665" y="455" width="175" height="595"/>
    <rect x="665" y="455" width="175" height="595" fill="url(#scene-fade)" role="img" aria-label="Soft grey sketch of a bakery kitchen counter"/>
  </g>

  <!-- ===== TOP FLAP, CONTENTS, BASE, RIGHT, BOTTOM PANELS ===== -->
  <path class="panel" d="M845,92 Q845,80 858,80 H1252 Q1265,80 1265,92 V270 H845 Z"/>
  <rect class="panel" x="840" y="250" width="425" height="205"/>
  <rect class="panel" x="840" y="455" width="425" height="595"/>
  <path class="panel" d="M1265,250 H1430 Q1442,250 1442,262 V440 H1265 Z"/>
  <rect class="panel" x="1265" y="440" width="180" height="620"/>
  <path class="panel" d="M1265,1060 H1442 V1238 Q1442,1250 1430,1250 H1265 Z"/>
  <rect class="panel" x="840" y="1050" width="425" height="200"/>
  <path class="panel" d="M845,1250 H1265 V1408 Q1265,1420 1252,1420 H858 Q845,1420 845,1408 Z"/>
  <rect x="853" y="462" width="400" height="573" fill="url(#scene-fade)" role="img" aria-label="Soft grey sketch of a bakery kitchen"/>

  <!-- ===== WATERCOLOUR WASHES, kept inside the dieline ===== -->
  <g class="washes" clip-path="url(#box-clip)" role="img" aria-label="Soft pastel watercolour splashes">
    <ellipse class="wash" cx="420" cy="520" rx="130" ry="80" fill="url(#wash-blue)"/>
    <ellipse class="wash" cx="215" cy="670" rx="90" ry="150" fill="url(#wash-pink)"/>
    <ellipse class="wash" cx="215" cy="800" rx="60" ry="90" fill="url(#wash-yellow)"/>
    <ellipse class="wash" cx="440" cy="900" rx="130" ry="70" fill="url(#wash-yellow)"/>
    <ellipse class="wash" cx="570" cy="760" rx="60" ry="120" fill="url(#wash-pink)"/>
    <ellipse class="wash" cx="690" cy="500" rx="45" ry="50" fill="url(#wash-yellow)"/>
    <ellipse class="wash" cx="750" cy="1130" rx="70" ry="45" fill="url(#wash-pink)"/>
    <ellipse class="wash" cx="1235" cy="130" rx="45" ry="90" fill="url(#wash-red)"/>
    <ellipse class="wash" cx="1060" cy="300" rx="110" ry="35" fill="url(#wash-blue)"/>
    <ellipse class="wash" cx="895" cy="560" rx="55" ry="65" fill="url(#wash-blue)"/>
    <ellipse class="wash" cx="900" cy="760" rx="55" ry="85" fill="url(#wash-red)"/>
    <ellipse class="wash" cx="1295" cy="620" rx="45" ry="100" fill="url(#wash-pink)"/>
    <ellipse class="wash" cx="1120" cy="1235" rx="100" ry="50" fill="url(#wash-red)"/>
    <ellipse class="wash" cx="1225" cy="1250" rx="45" ry="45" fill="url(#wash-yellow)"/>
  </g>

  <!-- ===== LID ARTWORK ===== -->
  <g class="lid-art">
    <rect x="252" y="472" width="170" height="180" rx="10" fill="url(#items-tone)" opacity="0.8" role="img" aria-label="Line drawing of eclair shells, powder pouch and piping bag"/>
    <ellipse cx="300" cy="822" rx="62" ry="108" fill="url(#pastry-tone)" role="img" aria-label="Photo of a chocolate glazed eclair cut open to show custard"/>

    <rect class="label-plate" x="345" y="612" width="210" height="262"/>
    <rect class="label-border" x="352" y="619" width="196" height="248"/>
    <rect class="label-plate" x="540" y="710" width="125" height="68"/>
    <g transform="translate(383,745) rotate(90)">
      <text class="kit-title kit-title--light" font-size="31" text-anchor="middle" dominant-baseline="central">THE ECLAIR KIT</text>
    </g>
    <g transform="translate(408,745) rotate(90)">
      <text class="presents" font-size="13" text-anchor="middle" dominant-baseline="central">presents</text>
    </g>
    <g transform="translate(475,745) rotate(90)">
      <rect x="-62" y="-44" width="124" height="88" rx="12" fill="#ffffff"/>
      <circle class="brand-dot" cx="0" cy="-22" r="7"/>
      <text class="brand-name" font-size="15" x="0" y="5" text-anchor="middle">Maison Lumière</text>
      <text class="brand-name" font-size="11" x="0" y="24" text-anchor="middle">BAKERY</text>
    </g>
  </g>

  <!-- ===== FRONT STRIP ARTWORK ===== -->
  <g class="front-art">
    <rect x="672" y="458" width="158" height="192" rx="10" fill="url(#items-tone)" opacity="0.8" role="img" aria-label="Line drawing of powder pouch and eclair shells"/>
    <rect class="label-plate" x="665" y="710" width="50" height="68"/>
    <ellipse cx="770" cy="755" rx="62" ry="100" fill="url(#pastry-tone)" role="img" aria-label="Photo of a chocolate eclair with custard filling"/>
    <g transform="translate(696,930) rotate(-90)">
      <text class="kit-title" font-size="22" text-anchor="middle" dominant-baseline="central">THE ECLAIR KIT</text>
    </g>
    <g transform="translate(776,930) rotate(-90)">
      <rect x="-56" y="-36" width="112" height="72" rx="10" fill="#ffffff"/>
      <circle class="brand-dot" cx="0" cy="-17" r="6"/>
      <text class="brand-name" font-size="12.5" x="0" y="5" text-anchor="middle">Maison Lumière</text>
      <text class="brand-name" font-size="9.5" x="0" y="21" text-anchor="middle">BAKERY</text>
    </g>
  </g>

  <!-- ===== CONTENTS PANEL ===== -->
  <g class="contents-side">
    <rect class="dotted-frame" x="853" y="285" width="400" height="150"/>
    <text class="kit-title" x="850" y="291" font-size="20" dominant-baseline="central">THE ECLAIR KIT</text>
    <rect x="850" y="303" width="105" height="36" rx="6" fill="url(#lettering-tone)" opacity="0.5" role="img" aria-label="Hand lettered heading: what's inside?"/>
    <rect x="870" y="350" width="130" height="44" rx="22" fill="url(#items-tone)" role="img" aria-label="Sketch of eclair shells"/>
    <rect x="1015" y="312" width="64" height="88" rx="4" fill="#f7c9a4" opacity="0.75" role="img" aria-label="Sketch of powder pouch"/>
    <path d="M1093,358 L1165,398 L1160,405 L1092,370 Z" fill="#e8c8d6" role="img" aria-label="Sketch of piping bag"/>
    <path d="M1186,380 L1208,402 L1186,405 Z" fill="#e6d77a" role="img" aria-label="Sketch of piping tip"/>
    <text class="item-label" x="903" y="420" text-anchor="middle">4 ECLAIR SHELLS</text>
    <text class="item-label" x="1003" y="420" text-anchor="middle">POWDER POUCH</text>
    <text class="item-label" x="1102" y="420" text-anchor="middle">PIPPING BAG &amp; PIPPING TIP</text>
    <text class="item-label" x="1202" y="420" text-anchor="middle">POWDER POUCH</text>
    <rect x="1170" y="295" width="78" height="58" rx="9" fill="#ffffff"/>
    <circle class="brand-dot" cx="1209" cy="309" r="6"/>
    <text class="brand-name" font-size="10" x="1209" y="328" text-anchor="middle">Maison Lumière</text>
    <text class="brand-name" font-size="8" x="1209" y="340" text-anchor="middle">BAKERY</text>
  </g>

  <!-- ===== BASE PANEL (instructions) ===== -->
  <g class="base">
    <rect class="dotted-frame" x="853" y="462" width="400" height="573"/>
    <rect x="935" y="452" width="70" height="12" rx="6" class="panel"/>
    <rect x="1100" y="452" width="70" height="12" rx="6" class="panel"/>
    <rect x="935" y="1034" width="70" height="12" rx="6" class="panel"/>
    <rect x="1100" y="1034" width="70" height="12" rx="6" class="panel"/>
    <rect x="930" y="520" width="270" height="450" rx="40" fill="var(--cocoa-soft)" opacity="0.85" role="img" aria-label="Brushed cocoa paint stroke background"/>

    <rect x="890" y="585" width="38" height="38" rx="10" fill="var(--hand-blue)" role="img" aria-label="Hand showing three fingers"/>
    <rect x="890" y="722" width="38" height="38" rx="10" fill="var(--hand-gold)" role="img" aria-label="Hand showing two fingers"/>
    <rect x="890" y="862" width="38" height="38" rx="10" fill="var(--hand-red)" role="img" aria-label="Hand showing one finger"/>

    <rect class="step-card" x="958" y="540" width="142" height="128"/>
    <g transform="translate(1029,604) rotate(-90)">
      <text class="step-text">
        <tspan x="-58" y="-60">Place icing in warm</tspan>
        <tspan x="-58" dy="13">water for 2 minutes, cut</tspan>
        <tspan x="-58" dy="13">bag at an angle, then</tspan>
        <tspan x="-58" dy="13">poor on top of eclair.</tspan>
      </text>
    </g>

    <rect class="step-card" x="958" y="678" width="142" height="124"/>
    <g transform="translate(1029,740) rotate(-90)">
      <text class="step-text">
        <tspan x="-58" y="-60">Place pipping tip in pip-</tspan>
        <tspan x="-58" dy="13">ping bag. Poor custard in</tspan>
        <tspan x="-58" dy="13">bag before cutting the tip</tspan>
        <tspan x="-58" dy="13">off of it off. Pipe custard</tspan>
        <tspan x="-58" dy="13">inside eclair by slightly</tspan>
        <tspan x="-58" dy="13">pressing on flat side of</tspan>
        <tspan x="-58" dy="13">the shell in 3 separate</tspan>
        <tspan x="-58" dy="13">areas for a more uniform</tspan>
        <tspan x="-58" dy="13">filling. Do not over fill or</tspan>
        <tspan x="-58" dy="13">shell will crack.</tspan>
      </text>
    </g>

    <rect class="step-card" x="958" y="810" width="142" height="126"/>
    <g transform="translate(1029,873) rotate(-90)">
      <text class="step-text">
        <tspan x="-58" y="-60">Mix powder patch with 1</tspan>
        <tspan x="-58" dy="13">cup of cold water, mix</tspan>
        <tspan x="-58" dy="13">for 2 minutes on high</tspan>
        <tspan x="-58" dy="13">speed. Let the custard</tspan>
        <tspan x="-58" dy="13">rest in fridge for 15 min-</tspan>
        <tspan x="-58" dy="13">utes.</tspan>
      </text>
    </g>

    <g transform="translate(1138,735) rotate(-90)">
      <text class="ingredients">
        <tspan x="-195" y="-22">Ingredients:</tspan>
        <tspan x="-195" dy="7.5">Eclair shell: wheat flour (gluten), butter fat 26 %, egg, water, potassium and sodium diphosphates, sodium carbonates, salt, sorbitol.</tspan>
        <tspan x="-195" dy="7.5">Powder: sugar, modified potato starch (E1414), whole milk powder, lactose and milk proteins, thickeners: calcium lactate, disodium</tspan>
        <tspan x="-195" dy="7.5">phosphate, sodium alginate, carrageenan, artificial and natural flavors: vanilla, caramel, colors: E 102, E 110.</tspan>
        <tspan x="-195" dy="7.5">(may contain cocoa powder) Icing: sugar, glucose syrup, water (may contain cocoa powder)</tspan>
      </text>
    </g>

    <g transform="translate(1190,852) rotate(-90)">
      <text class="kit-title" font-size="33" text-anchor="middle" dominant-baseline="central">THE ECLAIR KIT</text>
    </g>
    <g transform="translate(1205,580) rotate(-90)">
      <rect x="-40" y="-27" width="80" height="54" rx="9" fill="#ffffff"/>
      <circle class="brand-dot" cx="0" cy="-13" r="5.5"/>
      <text class="brand-name" font-size="9.5" x="0" y="4" text-anchor="middle">Maison Lumière</text>
      <text class="brand-name" font-size="7.5" x="0" y="15" text-anchor="middle">BAKERY</text>
    </g>
  </g>

  <!-- ===== RIGHT SIDE PANEL ===== -->
  <g class="right-side">
    <g transform="translate(1408,750) rotate(90)">
      <text class="kit-title" font-size="22" text-anchor="middle" dominant-baseline="central">THE ECLAIR KIT</text>
    </g>
    <g transform="translate(1340,742) rotate(90)">
      <rect x="-56" y="-38" width="112" height="76" rx="10" fill="#ffffff"/>
      <circle class="brand-dot" cx="0" cy="-19" r="7"/>
      <text class="brand-name" font-size="13" x="0" y="6" text-anchor="middle">Maison Lumière</text>
      <text class="brand-name" font-size="9.5" x="0" y="21" text-anchor="middle">BAKERY</text>
    </g>
  </g>

  <!-- ===== BOTTOM PANEL (nutrition) ===== -->
  <g class="nutrition-side">
    <g transform="rotate(180 1055 1100)">
      <rect x="855" y="1066" width="400" height="68" fill="#ffffff" stroke="#111" stroke-width="0.8"/>
      <text class="nutrition-head" x="858" y="1080">Nutrition Facts</text>
      <text class="nutrition" x="858" y="1090">Serving Size 1 Eclair (62g)</text>
      <text class="nutrition" x="858" y="1098">Servings Per Container 4</text>
      <text class="nutrition nutrition-bold" x="858" y="1108">Calories 262</text>
      <line x1="950" y1="1068" x2="950" y2="1112" stroke="#111" stroke-width="0.6"/>
      <text class="nutrition" x="954" y="1076"><tspan class="nutrition-bold">Total Fat</tspan> 13g 20%</text>
      <text class="nutrition" x="954" y="1085">Saturated Fat 8g 40%</text>
      <text class="nutrition" x="954" y="1094">Cholesterol 95mg 32%</text>
      <text class="nutrition" x="954" y="1103"><tspan class="nutrition-bold">Sodium</tspan> 210mg 9%</text>
      <text class="nutrition" x="1055" y="1076"><tspan class="nutrition-bold">Total Carbohydrate</tspan> 32g 11%</text>
      <text class="nutrition" x="1055" y="1085">Sugars 18g</text>
      <text class="nutrition" x="1055" y="1094"><tspan class="nutrition-bold">Protein</tspan> 5g</text>
      <line x1="855" y1="1114" x2="1255" y2="1114" stroke="#111" stroke-width="0.6"/>
      <text class="nutrition" x="858" y="1122">Vitamin D 0% Calcium 4% Iron 6%</text>
      <text class="nutrition" x="858" y="1130">*Percent Daily Values are based on a 2,000 calorie diet.</text>
    </g>
    <g transform="rotate(180 915 1200)">
      <text class="kit-title" x="915" y="1200" font-size="20" text-anchor="middle" dominant-baseline="central">THE ECLAIR KIT</text>
    </g>
    <g transform="translate(1212,1183) rotate(180)">
      <rect x="-40" y="-30" width="80" height="60" rx="9" fill="#ffffff"/>
      <circle class="brand-dot" cx="0" cy="-15" r="5.5"/>
      <text class="brand-name" font-size="9.5" x="0" y="4" text-anchor="middle">Maison Lumière</text>
      <text class="brand-name" font-size="7.5" x="0" y="16" text-anchor="middle">BAKERY</text>
    </g>
  </g>
</svg>
</body>
</html>
```